Book Cover " FROM CINDERBLOCK TO TARN"

Looking for a book cover for a novel FROM CINDERBLOCK TO TARN.
Tarn is the characters developed name. The book describes his rough up bringing and how he obtains his greatness and his given name Tarn.

```html
<!DOCTYPE html>
<html lang="en">
<head>
<meta charset="utf-8">
<title>From Cinderblock to Tarn — Book Cover</title>
<link rel="stylesheet" href="https://fonts.googleapis.com/css2?family=Cinzel:wght@400;500&display=swap">
<style>
  :root {
    --stage: #444444;
    --cover-black: #0b0b0c;
    --grit-black: #18181a;
    --silk-sheen: #5a5a5c;
    --silk-mid: #2a2a2c;
    --gold-light: #efe08a;
    --gold-mid: #c9a344;
    --gold-deep: #9a6f24;
    --frame-gold: #b8913a;
  }
  * { margin: 0; padding: 0; box-sizing: border-box; }
  html, body {
    width: 1200px;
    height: 1200px;
    overflow: hidden;
    background: var(--stage);
  }
  .canvas {
    position: relative;
    width: 1200px;
    height: 1200px;
    background: var(--stage);
  }
  .book-cover {
    position: absolute;
    left: 230px;
    top: 45px;
    width: 740px;
    height: 1110px;
    overflow: hidden;
    background: var(--cover-black);
    box-shadow: 0 20px 50px rgba(0,0,0,0.45);
  }
  .cover-art {
    position: absolute;
    inset: 0;
    background:
      radial-gradient(ellipse 60% 14% at 45% 62%, rgba(120,120,124,0.45), transparent 70%),
      radial-gradient(ellipse 45% 18% at 30% 82%, rgba(110,110,114,0.5), transparent 70%),
      radial-gradient(ellipse 40% 12% at 75% 90%, rgba(100,100,104,0.45), transparent 70%),
      linear-gradient(180deg,
        var(--grit-black) 0%,
        #202022 30%,
        var(--cover-black) 50%,
        var(--silk-mid) 66%,
        #111112 74%,
        var(--silk-sheen) 84%,
        #1a1a1b 93%,
        #3a3a3c 100%);
  }
  .title-frame {
    position: absolute;
    left: 86px;
    top: 430px;
    width: 580px;
    height: 300px;
    border: 2px solid var(--frame-gold);
    display: flex;
    flex-direction: column;
    align-items: center;
    justify-content: center;
  }
  .book-title {
    font-family: "Cinzel", "Trajan Pro", serif;
    font-weight: 400;
    font-size: 62px;
    line-height: 1.22;
    text-align: center;
    letter-spacing: 0.01em;
    background: linear-gradient(100deg, var(--gold-deep) 0%, var(--gold-light) 30%, var(--gold-mid) 55%, var(--gold-light) 75%, var(--gold-deep) 100%);
    -webkit-background-clip: text;
    background-clip: text;
    color: transparent;
  }
  .book-title span { display: block; }
  .author-name {
    position: absolute;
    left: 0;
    right: 0;
    top: 940px;
    text-align: center;
    font-family: "Cinzel", "Trajan Pro", serif;
    font-weight: 400;
    font-size: 28px;
    letter-spacing: 0.38em;
    color: var(--gold-mid);
  }
</style>
</head>
<body>
  <main class="canvas">
    <section class="book-cover">
      <div class="cover-art" role="img" aria-label="Black sandpaper grit texture fading into folds of draped black silk"></div>
      <div class="title-frame">
        <h1 class="book-title">
          <span>FROM</span>
          <span>CINDERBLOCK</span>
          <span>TO TARN</span>
        </h1>
      </div>
      <p class="author-name">AUTHOR NAME</p>
    </section>
  </main>
</body>
</html>
```